Religious Church Business Card Design

We need a business card design for our new pastor. We would like something warm and inviting. colors grape and white.
Updates

Church # 718-555-0139 and Cell # 718-555-0172

I also have a logo i tried to upload

Industry/Entity Type

Business

Contact Information for Business Card

Elder Ray Whitlock, Cedar Hollow Fellowship Church, 4172 Larkmoor Avenue, Bronx, NY 10982, email: raywhitlock@cedarhollowfellowship.example, www.cedarhollowfellowship.example

Colors
886aae

```html
<!DOCTYPE html>
<html lang="en">
<head>
<meta charset="utf-8">
<title>Elder Ray Whitlock – Business Card</title>
<link rel="stylesheet" href="https://fonts.googleapis.com/css2?family=Marcellus+SC&family=Tinos&display=swap">
<style>
  :root {
    --grape-deep: #3b1f63;
    --grape: #5a2d91;
    --grape-soft: #886aae;
    --logo-ink: #45325f;
    --paper: #ffffff;
    --paper-tint: #f1ebf5;
    --edge: #c9c9c9;
    --text-light: #ffffff;
  }
  * { margin: 0; padding: 0; box-sizing: border-box; }
  html, body {
    width: 1200px; height: 704px; overflow: hidden;
    background: var(--paper);
  }
  .canvas { position: relative; width: 1200px; height: 704px; }
  .card-art { position: absolute; inset: 0; }
  .logo-caption {
    position: absolute; left: 136px; top: 432px; width: 280px;
    text-align: center;
    font-family: "Marcellus SC", serif;
    font-size: 37px; line-height: 41px;
    color: var(--logo-ink);
  }
  .identity {
    position: absolute; right: 77px; top: 152px;
    text-align: right; color: var(--text-light);
    font-family: "Marcellus SC", serif;
  }
  .identity .name { font-size: 52px; line-height: 58px; letter-spacing: 0.5px; }
  .identity .church { font-size: 33px; line-height: 36px; letter-spacing: 1px; }
  .contact {
    position: absolute; right: 77px;
    text-align: right; color: var(--text-light);
    font-family: "Tinos", serif;
    font-size: 25px; line-height: 31px;
  }
  .contact.phones { top: 360px; }
  .contact.location { top: 527px; }
</style>
</head>
<body>
<main class="canvas">
  <svg class="card-art" width="1200" height="704" viewBox="0 0 1200 704" aria-hidden="false">
    <defs>
      <linearGradient id="paperFade" x1="0" y1="0" x2="1" y2="1">
        <stop offset="0" stop-color="var(--paper-tint)"/>
        <stop offset="1" stop-color="var(--paper)"/>
      </linearGradient>
      <linearGradient id="grapeFill" x1="0" y1="0" x2="1" y2="1">
        <stop offset="0" stop-color="#4e2688"/>
        <stop offset="0.5" stop-color="#4a2a80"/>
        <stop offset="1" stop-color="var(--grape-deep)"/>
      </linearGradient>
      <radialGradient id="patternGlow" cx="0.5" cy="0.5" r="0.5">
        <stop offset="0" stop-color="#7c55b3" stop-opacity="0.55"/>
        <stop offset="1" stop-color="#7c55b3" stop-opacity="0"/>
      </radialGradient>
    </defs>
    <rect class="card-paper" x="22" y="22" width="1156" height="660" fill="url(#paperFade)"/>
    <path class="wave-band" fill="var(--grape-soft)"
      d="M515 22 C440 70 445 210 462 330 C480 480 390 620 290 682 L1178 682 L1178 22 Z"/>
    <path class="grape-panel" fill="url(#grapeFill)"
      d="M545 22 C475 70 475 210 492 330 C510 480 430 620 336 682 L1178 682 L1178 22 Z"/>
    <ellipse class="pattern-area" role="img" aria-label="Faint decorative floral mandala pattern"
      cx="700" cy="330" rx="260" ry="320" fill="url(#patternGlow)"/>
    <g class="logo-cross" fill="var(--logo-ink)">
      <rect x="210" y="162" width="21" height="243"/>
      <rect x="130" y="229" width="179" height="21"/>
    </g>
    <rect class="card-edge" x="22.5" y="22.5" width="1155" height="659" fill="none" stroke="var(--edge)" stroke-width="1"/>
  </svg>

  <div class="logo-caption">Your<br>Church Logo</div>

  <header class="identity">
    <h1 class="name" style="font-weight:400">Elder Ray Whitlock</h1>
    <p class="church">Cedar Hollow Fellowship Church</p>
  </header>

  <p class="contact phones">Church: 718-555-0139<br>Cell: 718-555-0172</p>

  <p class="contact location">4172 Larkmoor Avenue, Bronx, NY 10982<br>raywhitlock@cedarhollowfellowship.example<br>www.cedarhollowfellowship.example</p>
</main>
</body>
</html>
```